Two Web Banners Needed for children product website! Fun and colorful!

My website is www.brightpebbletrinkets.com.au

I want 2 banners for the home page.

Size: 1920x1080px

Colors I like:
#BBA5D0
#FBF5BC
#F2BBAD

Text:
1) We create unique and meaningful gifts
2) We help you create happy memories

Fonts: provided in link

Brief:
1) I need two banners that showcase my two products on my website. I have images and fonts are included you can use in the files.
2) I want to capture child nature, friendliness and happiness.
3) I have also included samples of what I like
4) It's important to use some of the customer photographs too

Link to files:
https://filedrop-example.net/downloads/a1b2c3d4e5f60718293a4b5c6d7e8f9020220101000000/0f1e2d3c4b5a69788796a5b4c3d2e1f020220101000001/9z8y7x

If link does not work please PM me

Target Market(s)

Parents of children

Industry/Entity Type

Children ecommerce

Font styles to use
Other font styles liked:
• in file

Requirements
Must have
• Clean modern look

```html
<!DOCTYPE html>
<html lang="en">
<head>
<meta charset="utf-8">
<title>Children's gift banners</title>
<link rel="stylesheet" href="https://fonts.googleapis.com/css2?family=Allura&family=Montserrat:wght@700;800&family=Oswald:wght@200;300&display=swap">
<style>
:root{
  --board:#4d4c4e;
  --lilac:#bba5d0;
  --lilac-deep:#a994c4;
  --cream:#fbf5bc;
  --cream-soft:#fdf9d3;
  --blush:#f2bbad;
  --blush-deep:#e9aa9c;
  --salmon-btn:#efb2a1;
  --ink:#141414;
  --script-lilac:#a88fc8;
}
*{margin:0;padding:0;box-sizing:border-box}
html,body{width:923px;height:1200px;overflow:hidden;background:var(--board)}
.board{position:relative;width:923px;height:1200px;background:var(--board)}
.banner{position:absolute;left:61px;width:804px;height:451px;overflow:hidden;box-shadow:6px 10px 14px rgba(0,0,0,.45)}
.banner--memories{top:111px;background:var(--cream)}
.banner--gifts{top:646px;background:var(--blush)}
.banner__bg{position:absolute;inset:0;width:100%;height:100%}
.headline{position:absolute;color:var(--ink);line-height:1;white-space:nowrap}
.thin{font-family:"Oswald",sans-serif;font-weight:200;letter-spacing:-1px}
.bold{font-family:"Montserrat",sans-serif;font-weight:800}
.script{font-family:"Allura",cursive;font-weight:400}
.btn{position:absolute;width:162px;height:36px;border-radius:6px;display:flex;align-items:center;justify-content:center;font-family:"Montserrat",sans-serif;font-weight:700;font-size:21px;color:var(--ink)}
.btn--salmon{left:89px;top:319px;background:var(--salmon-btn)}
.btn--lilac{left:121px;top:319px;background:var(--lilac)}
.photo{position:absolute;border-radius:4px}
</style>
</head>
<body>
<div class="board">

  <section class="banner banner--memories">
    <svg class="banner__bg" viewBox="0 0 804 451" preserveAspectRatio="none" aria-hidden="true">
      <circle cx="40" cy="40" r="90" fill="var(--cream-soft)"/>
      <path d="M150 0 C190 60 280 80 340 0" fill="none" stroke="#e6dfa6" stroke-width="1"/>
      <path d="M120 0 C170 80 300 100 370 0" fill="none" stroke="#e6dfa6" stroke-width="1"/>
      <path d="M0 370 C130 330 260 430 420 400 C540 378 610 300 700 255 C760 225 790 150 804 95 L804 451 L0 451Z" fill="var(--lilac)"/>
      <path d="M0 451 L0 425 C110 405 220 430 320 451Z" fill="var(--lilac-deep)" opacity=".5"/>
      <path d="M600 451 C650 400 720 380 804 360" fill="none" stroke="#9d88b8" stroke-width="1"/>
      <path d="M640 451 C690 415 750 400 804 395" fill="none" stroke="#9d88b8" stroke-width="1"/>
    </svg>
    <div class="headline thin" style="left:43px;top:52px;font-size:66px">We Help You</div>
    <div class="headline bold" style="left:40px;top:112px;font-size:70px">Create</div>
    <div class="headline script" style="left:85px;top:163px;font-size:82px;color:var(--script-lilac)">Happy</div>
    <div class="headline bold" style="left:20px;top:229px;font-size:49px">MEMORIES</div>
    <div class="btn btn--salmon">Shop now</div>
    <div class="photo" role="img" aria-label="Two smiling toddlers beside personalised upholstered children's chairs in burgundy, grey and blue embroidered with names" style="left:320px;top:31px;width:484px;height:404px;background:linear-gradient(120deg,#7a2446 0%,#3a6fb8 35%,#c9c8c6 60%,#2a3ea8 100%);opacity:.85"></div>
  </section>

  <section class="banner banner--gifts">
    <svg class="banner__bg" viewBox="0 0 804 451" preserveAspectRatio="none" aria-hidden="true">
      <path d="M0 0 L200 0 C260 80 180 160 60 180 C30 185 10 190 0 195Z" fill="var(--blush-deep)" opacity=".35"/>
      <path d="M804 190 C700 225 620 320 560 360 C500 400 420 410 370 451 L804 451Z" fill="var(--cream)"/>
      <path d="M0 451 L0 405 C100 380 200 420 280 451Z" fill="var(--cream)"/>
      <path d="M620 0 C650 40 700 50 740 0" fill="none" stroke="#d99c8e" stroke-width="1"/>
      <path d="M600 0 C640 60 720 70 770 0" fill="none" stroke="#d99c8e" stroke-width="1"/>
    </svg>
    <div class="headline script" style="left:109px;top:20px;font-size:70px">We Create</div>
    <div class="headline thin" style="left:44px;top:76px;font-size:82px">Unique and</div>
    <div class="headline bold" style="left:36px;top:161px;font-size:49px">Meaningful</div>
    <div class="headline script" style="left:120px;top:196px;font-size:110px">Gifts</div>
    <div class="btn btn--lilac">Shop now</div>
    <div class="photo" role="img" aria-label="Green and pink slap bracelets with dinosaur and unicorn charms" style="left:21px;top:231px;width:77px;height:208px;background:linear-gradient(90deg,#5cc4a8 0 45%,transparent 45% 55%,#d8357e 55%)"></div>
    <div class="photo" role="img" aria-label="Two mini fingerboard skateboard keychains" style="left:290px;top:319px;width:88px;height:108px;background:linear-gradient(90deg,#3aa9a0,#9a9aa6)"></div>
    <div class="photo" role="img" aria-label="Personalised spot-the-difference activity sheet with a child's photo" style="left:398px;top:23px;width:154px;height:354px;background:linear-gradient(180deg,#f2f1ee,#e8e6ea)"></div>
    <div class="photo" role="img" aria-label="Sheet of round personalised photo stickers" style="left:581px;top:31px;width:211px;height:127px;background:#f4eecb"></div>
    <div class="photo" role="img" aria-label="Star-topped bubble wands in orange, pink, blue and green" style="left:401px;top:323px;width:77px;height:112px;background:linear-gradient(90deg,#f07a2a,#e0508e,#3a9fd8,#4bbf5a)"></div>
    <div class="photo" role="img" aria-label="Blue bubble wand and skateboard keychain" style="left:571px;top:173px;width:62px;height:104px;background:linear-gradient(90deg,#3aa0d0,#c9c8d0)"></div>
    <div class="photo" role="img" aria-label="Kraft box of pencils with a personalised photo label" style="left:559px;top:285px;width:65px;height:96px;background:#cfae7e"></div>
    <div class="photo" role="img" aria-label="Personalised space-themed spiral notebook" style="left:636px;top:169px;width:158px;height:211px;background:linear-gradient(160deg,#4a5fa8,#6a78bd)"></div>
  </section>

</div>
</body>
</html>
```